New E-Learning Website Design Wanted!

I am creating an E-learning website for those interested in getting certifications in the IT industry.
For example, courses related to BKX, Pellin, RTM certifications and national certifications in the IT industry in Japan will be offered.
You can think of sites such as Pindoval, Fevly, VexaPoint, Bintorum.
But I am targeting industries in Japan at the moment.
Also, I have uploaded screenshots of pages that I think are good.

The company is Solvik Data
I recently got my company logo designed so I attached pdf file to this project brief.
I would appreciate it if you can make the site match the color scheme of the logo.

Target Market(s)

I am targeting individuals as well as large IT companies in Japan

Industry/Entity Type

Education

Coding

Coded - Design and coding required

Number of Pages Required

4 page

Font styles to use
Sans Serif

Colors

Designer to choose colors to be used in the design.

Requirements
Must have
• One top page design
• One course page (https://vexapt.test/courses/pellor-grid-systems)
• One learning page(where the learner can see the video)
• One blog page(https://news.vexapt.test/resources?_ga=2.36414185.89678801.1578174478-594719062.1578174478)
Nice to have
• Pricing page

```html
<!DOCTYPE html>
<html lang="en">
<head>
<meta charset="utf-8">
<title>Flarion Tutorial Step by Step – Solvik Data</title>
<link href="https://fonts.googleapis.com/css2?family=Poppins:wght@300;400;500;600;700&display=swap" rel="stylesheet">
<style>
:root{
  --navy:#15234f;
  --ink:#1f2a44;
  --blue:#1d5c8f;
  --teal:#1ea093;
  --muted:#8a93a3;
  --label:#7b8494;
  --line:#e6e9ee;
  --panel-grey:#f3f4f6;
  --white:#ffffff;
}
*{box-sizing:border-box;margin:0;padding:0}
html,body{width:1200px;height:2501px;overflow:hidden;background:var(--white)}
body{font-family:'Poppins',sans-serif;color:var(--ink)}
.page{position:relative;width:1200px;height:2501px;overflow:hidden}
.abs{position:absolute}

/* header */
.brand{left:88px;top:66px;font-size:19px;font-weight:400;color:var(--blue);letter-spacing:.5px;display:flex;align-items:center;gap:8px}
.brand .dot{width:12px;height:12px;border-radius:50%;background:var(--teal)}
.course-title{left:307px;top:37px;font-size:15px;font-weight:500}
.rating{left:670px;top:36px;font-size:15px;font-weight:500;display:flex;align-items:center;gap:6px}
.progress{left:818px;top:28px;display:flex;align-items:center;gap:10px;font-size:15px;font-weight:500;color:#6b7280}
.progress .ring{width:38px;height:38px;border-radius:50%;border:3px solid #dfe3e8;display:flex;align-items:center;justify-content:center}
.share{left:1004px;top:29px;width:86px;height:36px;border-radius:18px;background:var(--teal);color:#fff;font-size:15px;font-weight:600;display:flex;align-items:center;justify-content:center;gap:5px}
.kebab{left:1106px;top:34px;display:flex;flex-direction:column;gap:4px}
.kebab i{width:5px;height:5px;border-radius:50%;background:#6b7280;display:block}

/* player */
.player{left:89px;top:118px;width:706px;height:466px;border-radius:16px;overflow:hidden;background:radial-gradient(circle at 50% 55%,#7a2ff0 0%,#5a16c9 45%,#2a0a7a 100%)}
.player .art{position:absolute;left:150px;top:120px;width:390px;height:230px;border-radius:50%;background:linear-gradient(160deg,#ffffff,#dfe6f5)}
.player .play{position:absolute;left:306px;top:185px;width:82px;height:82px;border-radius:50%;background:rgba(90,90,100,.75)}
.player .play:after{content:"";position:absolute;left:33px;top:26px;border-left:24px solid #fff;border-top:15px solid transparent;border-bottom:15px solid transparent}
.nav-arrow{position:absolute;top:197px;width:32px;height:70px;background:rgba(30,10,70,.6);color:#fff;font-size:14px;display:flex;align-items:center;justify-content:center}

/* tabs */
.tabs{left:89px;top:600px;width:707px;height:40px;border-bottom:1px solid var(--line);display:flex;align-items:center;font-size:14px;font-weight:600;color:#4b5563}
.tabs span{padding:0 15px;height:40px;display:flex;align-items:center}
.tabs .active{color:var(--teal);border-bottom:3px solid var(--teal);margin-left:6px;padding:0 12px}

.h-about{left:88px;top:690px;font-size:28px;font-weight:700;color:var(--navy)}
.about-sub{left:88px;top:726px;font-size:14px;color:var(--muted)}
.rule{left:89px;width:707px;height:1px;background:var(--line)}
.row-label{left:88px;font-size:15px;font-weight:600;color:var(--label)}
.numbers{left:271px;top:832px;font-size:14px;line-height:23.2px;color:var(--muted)}
.numbers b{font-weight:500;color:#3b4456}
.feature{top:1042px;font-size:15px;color:#4b5563;white-space:nowrap}
.desc{left:271px;top:1131px;width:500px;font-size:15px;line-height:22px;color:#4b5563}
.desc span{color:#b5bbc6}
.see-more{left:267px;top:1181px;font-size:18px;font-weight:600;color:var(--teal)}

.h-similar{left:88px;top:1253px;font-size:32px;font-weight:700;color:var(--navy)}
.card{top:1308px;width:172px;height:230px;border-radius:10px;background:#fff;box-shadow:0 2px 10px rgba(20,30,60,.08);padding:6px}
.card .thumb{height:127px;border-radius:6px}
.card h4{margin:12px 8px 0;font-size:12px;line-height:16px;font-weight:600;color:var(--navy)}
.card p{margin:4px 8px 0;font-size:10.5px;color:var(--muted)}
.card .start{display:inline-block;margin:6px 8px 0;padding:3px 8px;border-radius:10px;background:#eef0f3;font-size:9px;font-weight:600;color:var(--teal)}
.card-next{left:778px;top:1378px;width:40px;height:40px;border-radius:50%;background:#fff;box-shadow:0 2px 8px rgba(20,30,60,.15);display:flex;align-items:center;justify-content:center;font-size:14px}

.teach{left:89px;top:1607px;width:706px;height:152px;border-radius:16px;background:linear-gradient(90deg,#1d4f85 0%,#1d7b92 55%,#1ea59a 100%);color:#fff;z-index:2}
.teach .globe{position:absolute;left:30px;top:40px;width:72px;height:72px;border-radius:50%;background:radial-gradient(circle at 40% 40%,#bfe6ee,#3f9d6a)}
.teach h3{position:absolute;left:115px;top:38px;font-size:27px;font-weight:700}
.teach p{position:absolute;left:115px;top:80px;width:430px;font-size:15.5px;line-height:21px}
.teach .btn{position:absolute;left:544px;top:60px;width:140px;height:38px;border-radius:19px;background:#fff;color:var(--navy);font-size:13px;font-weight:500;display:flex;align-items:center;justify-content:center}

/* footer */
.footer-shape{left:0;top:0;z-index:1}
.news-h{left:0;top:1948px;width:1200px;text-align:center;font-size:38px;line-height:43px;font-weight:700;color:#fff;z-index:2}
.subscribe{left:240px;top:2053px;width:718px;height:52px;border-radius:26px;background:#fff;border:2px solid #fff;z-index:2}
.subscribe span{position:absolute;left:24px;top:14px;font-size:15px;color:#8a93a3}
.subscribe .btn{position:absolute;right:0;top:0;width:180px;height:48px;border-radius:24px;background:var(--teal);color:#fff;font-size:17px;font-weight:700;display:flex;align-items:center;justify-content:center;letter-spacing:.5px}
.f-brand{left:110px;top:2290px;width:310px;text-align:center;z-index:2;color:#fff}
.f-brand .name{font-size:34px;font-weight:400;letter-spacing:1.5px}
.f-brand p{margin-top:6px;font-size:14px;line-height:23px;color:#d6dbe8}
.f-col{top:2198px;z-index:2;color:#fff}
.f-col h5{font-size:19px;font-weight:700;margin-bottom:8px}
.f-col a{display:block;font-size:14px;line-height:26px;color:#d6dbe8;text-decoration:none}
.f-rule{left:89px;top:2452px;width:1022px;height:1px;background:rgba(255,255,255,.12);z-index:2}
.copy{left:88px;top:2466px;font-size:14px;color:#fff;z-index:2}
.socials{left:1020px;top:2472px;display:flex;gap:12px;z-index:2}
.socials i{width:12px;height:12px;border-radius:50%;background:#fff;display:block}
.to-top{left:1134px;top:2430px;width:34px;height:34px;border-radius:50%;background:var(--teal);z-index:2;display:flex;align-items:center;justify-content:center;color:#fff;font-size:12px}

/* sidebar */
.sidebar{left:822px;top:120px;width:282px;height:700px;background:#fff;border-radius:12px;box-shadow:0 4px 22px rgba(20,30,60,.07)}
.sb-title{left:844px;top:154px;font-size:18px;font-weight:600;color:var(--blue)}
.sb-close{left:1066px;top:154px;font-size:20px;color:#6b7280;font-weight:300}
.sec{left:846px;width:238px;font-size:14px;color:var(--blue);font-weight:500}
.sec small{display:block;font-size:12px;font-weight:400;color:#5b6474;margin-top:-1px}
.sec .chev{position:absolute;right:0;top:8px;width:8px;height:8px;border-right:2px solid var(--navy);border-bottom:2px solid var(--navy);transform:rotate(45deg)}
.sec .chev.up{transform:rotate(-135deg);top:12px}
.sb-line{left:843px;width:240px;height:1px;background:var(--line)}
.lessons{left:822px;top:328px;width:282px;height:172px;background:var(--panel-grey)}
.lesson{position:absolute;left:26px;font-size:12.5px;color:#3b4456;line-height:16px}
.lesson .tick{position:absolute;left:0;top:1px;width:13px;height:13px;border-radius:50%;background:var(--teal)}
.lesson .tick:after{content:"";position:absolute;left:4px;top:2px;width:3px;height:6px;border-right:2px solid #fff;border-bottom:2px solid #fff;transform:rotate(45deg)}
.lesson .txt{margin-left:22px;display:block}
.lesson .dur{margin-left:22px;display:block;color:#6b7280;margin-top:3px}
</style>
</head>
<body>
<div class="page">

  <!-- header -->
  <div class="abs brand"><span class="dot"></span>Solvik Data</div>
  <div class="abs course-title">Flarion Tutorial Step by Step</div>
  <div class="abs rating"><svg width="14" height="14" viewBox="0 0 24 24"><path fill="#f5a623" d="M12 2l3 7 7 .6-5.3 4.7 1.6 7.3L12 17.8 5.7 21.6l1.6-7.3L2 9.6 9 9z"/></svg>Leave a rating</div>
  <div class="abs progress"><span class="ring"><svg width="16" height="16" viewBox="0 0 24 24"><path fill="#b8bec8" d="M6 3h12v3h3v3a5 5 0 0 1-5 5 6 6 0 0 1-3 2v3h4v2H7v-2h4v-3a6 6 0 0 1-3-2 5 5 0 0 1-5-5V6h3z"/></svg></span>Your Progress ⌄</div>
  <div class="abs share"><svg width="13" height="13" viewBox="0 0 24 24"><path fill="#fff" d="M14 4l8 7-8 7v-4c-6 0-9 2-12 6 1-6 4-11 12-12z"/></svg>Share</div>
  <div class="abs kebab"><i></i><i></i><i></i></div>

  <!-- player -->
  <div class="abs player">
    <div class="art" role="img" aria-label="Course cover artwork: tutorials contributor badge with graduation cap on purple hexagon background"></div>
    <div class="play"></div>
    <div class="nav-arrow" style="left:0">‹</div>
    <div class="nav-arrow" style="right:0">›</div>
  </div>

  <!-- tabs -->
  <div class="abs tabs">
    <svg width="18" height="18" viewBox="0 0 24 24" style="margin-left:2px"><circle cx="10" cy="10" r="7" fill="none" stroke="#1ea093" stroke-width="2.5"/><path d="M15 15l6 6" stroke="#1ea093" stroke-width="2.5"/></svg>
    <span class="active">Overview</span><span>Q&amp;A</span><span>Bokmarks</span><span>Announcements</span>
  </div>

  <div class="abs h-about">About this course</div>
  <div class="abs about-sub">Learn to create&nbsp; your first website and Restful API using pyrel anf Flarion.</div>
  <div class="abs rule" style="top:795px"></div>

  <div class="abs row-label" style="top:830px">By the numbers</div>
  <div class="abs numbers">
    <b>By the numbers Skill level:</b> Intermediate<br>
    <b>Lectures:</b> 19 Level<br>
    <b>Video:</b> 2 hours<br>
    <b>Students:</b> 30713<br>
    <b>Languages:</b> English<br>
    <b>Captions:</b> Yes
  </div>
  <div class="abs rule" style="top:1003px"></div>

  <div class="abs row-label" style="top:1034px">Features</div>
  <div class="abs feature" style="left:271px">Available on Orbit OS and Droidra</div>
  <div class="abs feature" style="left:555px">Certificate of completion</div>
  <div class="abs rule" style="top:1091px"></div>

  <div class="abs row-label" style="top:1130px">Description</div>
  <div class="abs desc">Flarion Tutorial - Step By Step This is a comprehensive step by step <span>guide that will walk you</span></div>
  <div class="abs see-more">+ See more</div>

  <div class="abs h-similar">Similar courses</div>
  <div class="abs card" style="left:89px"><div class="thumb" role="img" aria-label="Data scientist isometric illustration" style="background:linear-gradient(135deg,#f4f6fb,#7aa7f0)"></div><h4>BKX Certified Solutions Architect Associate</h4><p>119 lessons • 12.5 hrs total</p><span class="start">Start Course</span></div>
  <div class="abs card" style="left:268px"><div class="thumb" role="img" aria-label="Cloud storage illustration" style="background:linear-gradient(135deg,#5a1bb0,#2d3fd6)"></div><h4>BKX Certified Solutions Architect Associate</h4><p>119 lessons • 12.5 hrs total</p><span class="start">Start Course</span></div>
  <div class="abs card" style="left:447px"><div class="thumb" role="img" aria-label="Business laptop illustration" style="background:linear-gradient(135deg,#2a8fe0,#1d4fb8)"></div><h4>BKX Certified Solutions Architect Associate</h4><p>119 lessons • 12.5 hrs total</p><span class="start">Start Course</span></div>
  <div class="abs card" style="left:627px"><div class="thumb" role="img" aria-label="Data cubes isometric illustration" style="background:linear-gradient(135deg,#2548c8,#1a2a8a)"></div><h4>BKX Certified Solutions Architect Associate</h4><p>119 lessons • 12.5 hrs total</p><span class="start">Start Course</span></div>
  <div class="abs card-next">›</div>

  <div class="abs teach">
    <div class="globe" role="img" aria-label="Globe illustration"></div>
    <h3>Tech The World Online</h3>
    <p>Create an online Video Course, reach students across the globe, and earn money</p>
    <div class="btn">Teach on Solvik</div>
  </div>

  <!-- footer -->
  <svg class="abs footer-shape" width="1200" height="2501" viewBox="0 0 1200 2501">
    <path fill="#1b2657" d="M0 1785 L360 1895 Q420 1905 425 1870 L380 1835 L645 1752 L665 1765 L690 1752 L1020 1880 Q1040 1895 1030 1910 L1200 1995 L1200 2501 L0 2501 Z"/>
    <path fill="#1f2c60" d="M0 2080 L300 2250 L500 2420 L540 2501 L0 2501 Z" opacity=".6"/>
  </svg>
  <div class="abs news-h">Want us to email you occasionally<br>with Solvik Data news?</div>
  <div class="abs subscribe"><span>Enter your email addres</span><div class="btn">SUBSCRIBE</div></div>

  <div class="abs f-brand"><div class="name">Solvik Data</div><p>Lorem Ipsum is simply dummy text of the printing and typesetting industry.</p></div>
  <div class="abs f-col" style="left:533px"><h5>LEARN</h5><a>Sign Up</a><a>Sign In</a><a>Browse</a><a>Index</a><a>Commercial</a></div>
  <div class="abs f-col" style="left:729px"><h5>DISCUSS</h5><a>Forum</a><a>Podcast</a><a>Blog</a><a>Support</a></div>
  <div class="abs f-col" style="left:943px"><h5>EXTRAS</h5><a>Testimonials</a><a>FAQ</a><a>Assets</a><a>Get a Job</a><a>Privacy</a><a>Terms</a></div>
  <div class="abs f-rule"></div>
  <div class="abs copy">Copyright 2019 | All Rights Reserved</div>
  <div class="abs socials"><i></i><i></i><i></i><i></i></div>
  <div class="abs to-top">^</div>

  <!-- sidebar -->
  <div class="abs sidebar"></div>
  <div class="abs sb-title">Course Content</div>
  <div class="abs sb-close">✕</div>
  <div class="abs sb-line" style="top:196px"></div>
  <div class="abs sec" style="top:212px">Section 1: Introduction<small>1 / 1 | 5 min</small><span class="chev"></span></div>
  <div class="abs sb-line" style="top:262px"></div>
  <div class="abs sec" style="top:281px">Section 2 : Before We Begin<small>1 / 2 | 11 min</small><span class="chev up"></span></div>
  <div class="abs lessons">
    <div class="lesson" style="top:25px"><span class="tick"></span><span class="txt">2.Understand&nbsp; HTTP</span><span class="dur">▸ 7 min</span></div>
    <div style="position:absolute;left:22px;top:77px;width:240px;height:1px;background:#e1e4e9"></div>
    <div class="lesson" style="top:98px"><span class="tick"></span><span class="txt">3. Step 00 - Setting up our<br>first Application</span><span class="dur">▸ 7 min</span></div>
  </div>
  <div class="abs sec" style="top:522px">Section 3 : Flarion basis<small>1 / 1 | 5 min</small><span class="chev"></span></div>
  <div class="abs sb-line" style="top:573px"></div>
  <div class="abs sec" style="top:592px">Section 4: Introduction<small>1 / 1 | 5 min</small><span class="chev"></span></div>
  <div class="abs sb-line" style="top:644px"></div>
  <div class="abs sec" style="top:663px">Section 1: Introduction<small>1 / 1 | 5 min</small><span class="chev"></span></div>
  <div class="abs sb-line" style="top:715px"></div>
  <div class="abs sec" style="top:735px">Section 1: Introduction<small>1 / 1 | 5 min</small><span class="chev"></span></div>
  <div class="abs sb-line" style="top:786px"></div>

</div>
</body>
</html>
```